Business Card Design for my Real Estate Investing Company

This is for a Real Estate Investing Company that will be serving the Las Vegas Valley. Id like the following slogan included: "Investing in Our Community" I have attached my logo. You will see the color tones I'm interested in..in my logo. I would like the card to be double-sided with a modern, professional look.
Target Market(s)
Homeowners, banks, real estate industry
Industry/Entity Type
Real Estate
Contact Information for Business Card
name: Dale Pruitt
position: Managing Member
address: 4812 Corvane Pkwy ste 207-300
N. Las Vegas, NV 89517
phone: (702) 555-0143
fax: (702) 555-0187
email: OakridgeHousePurchaser@examplemail.com
web: OakridgeHousePurchasers.example
*At the bottom of the card I would like....
We buy houses for cash....no repairs, no commissions, no fees!
Logo Text
OAKRIDGE HOUSE PURCHASERS "Investing in Our Community"
Font styles to use
Other font styles liked:
- Lora
Requirements
Must have
- On the back of the card, i'd like to have my logo large and the following statements:
- Are you considering selling your home? Want a simple, hassle-free transaction? We can help! We buy houses for cash and can close quickly! No need to do any repairs, no realtor commissions, no closing costs.....and no headaches. Let us help you with your real estate needs...!
Nice to have
- multiple colors 2 two tone on front and back

```html
<!DOCTYPE html>
<html lang="en">
<head>
<meta charset="utf-8">
<title>Oakridge House Purchasers – Business Card</title>
<link rel="stylesheet" href="https://fonts.googleapis.com/css2?family=Lora:ital,wght@0,400;0,600;0,700;1,400&display=swap">
<style>
  :root {
    --brand-blue: #1a6fc0;
    --soft-grey: #c9cbce;
    --ink: #2b2b2b;
    --paper: #f6f7f8;
    --backdrop: #e4e5e7;
  }
  * { box-sizing: border-box; margin: 0; padding: 0; }
  html, body { width: 1200px; height: 780px; overflow: hidden; }
  body {
    background: var(--backdrop);
    font-family: "Lora", Georgia, serif;
    color: var(--ink);
    display: flex;
    align-items: center;
    justify-content: center;
    gap: 40px;
  }
  .card {
    position: relative;
    width: 540px;
    height: 309px;
    background: linear-gradient(160deg, #ffffff 0%, var(--paper) 100%);
    box-shadow: 0 6px 18px rgba(0,0,0,0.18);
    overflow: hidden;
  }
  .card-waves { position: absolute; inset: 0; width: 100%; height: 100%; }

  .holder { position: absolute; left: 28px; top: 34px; }
  .holder-name {
    color: var(--brand-blue);
    font-weight: 700;
    font-size: 19px;
    letter-spacing: 0.5px;
    text-transform: uppercase;
  }
  .holder-title { color: #555; font-size: 13px; margin-top: 2px; }

  .brand {
    position: absolute;
    display: flex;
    align-items: center;
    gap: 7px;
    white-space: nowrap;
  }
  .brand-mark {
    flex: none;
    background: var(--brand-blue);
  }
  .brand-name {
    color: var(--brand-blue);
    font-weight: 600;
    line-height: 1;
    letter-spacing: 0.5px;
  }

  .card-front .brand { right: 26px; top: 38px; }
  .card-front .brand-mark { width: 11px; height: 11px; }
  .card-front .brand-name { font-size: 17px; }

  .address {
    position: absolute;
    right: 26px;
    top: 112px;
    text-align: right;
    font-size: 12.5px;
    font-style: normal;
    line-height: 1.35;
    color: #333;
  }

  .contacts {
    position: absolute;
    left: 28px;
    top: 168px;
    list-style: none;
    font-size: 12px;
    line-height: 1.45;
    color: #333;
  }
  .contacts li { display: flex; align-items: center; gap: 7px; }
  .contacts svg { width: 13px; height: 13px; flex: none; }

  .card-back .brand {
    left: 50%; top: 100px;
    transform: translateX(-50%);
  }
  .card-back .brand-mark { width: 15px; height: 15px; }
  .card-back .brand-name { font-size: 26px; }
</style>
</head>
<body>

  <section class="card card-front" aria-label="Front of business card">
    <svg class="card-waves" viewBox="0 0 540 309" aria-hidden="true">
      <path d="M0,258 C190,260 380,238 540,150 L540,309 L0,309 Z" fill="var(--soft-grey)"/>
      <path d="M0,276 C200,278 390,256 540,178 L540,309 L0,309 Z" fill="var(--brand-blue)"/>
      <path id="slogan-path" d="M150,300 C290,294 410,266 532,206" fill="none"/>
      <text fill="#ffffff" font-family="Lora, Georgia, serif" font-size="12.5" letter-spacing="0.3">
        <textPath href="#slogan-path">We buy houses for cash....no repairs, no commissions, no fees</textPath>
      </text>
    </svg>

    <div class="holder">
      <p class="holder-name">Dale Pruitt</p>
      <p class="holder-title">Managing Member</p>
    </div>

    <div class="brand">
      <span class="brand-mark"></span>
      <p class="brand-name">OAKRIDGE HOUSE PURCHASERS</p>
    </div>

    <address class="address">
      4812 Corvane Pkwy ste 207-300<br>
      N. Las Vegas, NV 89517
    </address>

    <ul class="contacts">
      <li>
        <svg viewBox="0 0 14 14" aria-label="Phone"><rect width="14" height="14" fill="var(--brand-blue)"/><path d="M4 3 L6 3 L6.5 5 L5.3 5.8 C5.9 7 6.9 8 8.2 8.7 L9 7.5 L11 8 L11 10 C7 10.5 3.5 7 4 3 Z" fill="#fff"/></svg>
        (702) 555-0143
      </li>
      <li>
        <svg viewBox="0 0 14 14" aria-label="Fax"><rect width="14" height="14" fill="var(--brand-blue)"/><rect x="4" y="2.5" width="6" height="3.5" fill="#fff"/><rect x="2.5" y="6" width="9" height="4" fill="#fff"/><rect x="4" y="9" width="6" height="2.5" fill="#fff"/></svg>
        (702) 555-0187
      </li>
      <li>
        <svg viewBox="0 0 14 14" aria-label="Email"><rect width="14" height="14" fill="var(--brand-blue)"/><rect x="2.5" y="4" width="9" height="6" fill="#fff"/><path d="M2.5 4 L7 7.5 L11.5 4" stroke="var(--brand-blue)" stroke-width="1" fill="none"/></svg>
        OakridgeHousePurchaser@examplemail.com
      </li>
      <li>
        <svg viewBox="0 0 14 14" aria-label="Website"><rect width="14" height="14" fill="var(--brand-blue)"/><circle cx="7" cy="7" r="4.2" fill="none" stroke="#fff" stroke-width="1"/><ellipse cx="7" cy="7" rx="1.8" ry="4.2" fill="none" stroke="#fff" stroke-width="0.8"/><path d="M2.8 7 H11.2" stroke="#fff" stroke-width="0.8"/></svg>
        OakridgeHousePurchasers.example
      </li>
    </ul>
  </section>

  <section class="card card-back" aria-label="Back of business card">
    <svg class="card-waves" viewBox="0 0 540 309" aria-hidden="true">
      <path d="M0,186 C150,240 350,272 540,282 L540,309 L0,309 Z" fill="var(--soft-grey)"/>
      <path d="M0,204 C150,254 350,282 540,292 L540,309 L0,309 Z" fill="var(--brand-blue)"/>
      <path id="web-path" d="M60,262 C150,284 250,296 360,302" fill="none"/>
      <text fill="#ffffff" font-family="Lora, Georgia, serif" font-size="12.5">
        <textPath href="#web-path">OakridgeHousePurchasers.example</textPath>
      </text>
    </svg>

    <div class="brand">
      <span class="brand-mark"></span>
      <p class="brand-name">OAKRIDGE HOUSE PURCHASERS</p>
    </div>
  </section>

</body>
</html>
```